Pelmora needs stationery design

We need desings for presentation cards and letter head for our company. It would be better that the letterhead uses our logo with white background and the presentation card the logo with the black background for the back of the card and the text (name, phone
Updates

Necesitas un par de días antes de escoger al ganador

Colors
0455a3
ec1f27
000000

Requirements
Must have
• Use company logo and colors

```html
<!DOCTYPE html>
<html lang="en">
<head>
<meta charset="utf-8">
<title>Pelmora Stationery</title>
<link href="https://fonts.googleapis.com/css2?family=Open+Sans:wght@400;600;700&family=Tinos&display=swap" rel="stylesheet">
<style>
  :root {
    --blue: #0455a3;
    --red: #ec1f27;
    --black: #1b1c1e;
    --ink: #2a2a2a;
    --muted: #555;
    --backdrop: #aaa9aa;
    --paper: #efefef;
  }
  html, body { margin: 0; padding: 0; width: 1200px; height: 1030px; overflow: hidden; background: var(--backdrop); }
  .stage { position: relative; width: 1256px; height: 1078px; transform: scale(0.9554); transform-origin: 0 0; font-family: "Open Sans", sans-serif; }
  .sheet { position: absolute; box-shadow: 0 0 3px rgba(0,0,0,.35); }
  .letterhead { left: 96px; top: 81px; width: 652px; height: 917px; background: linear-gradient(90deg, #f5f5f5 0%, #e8e8e8 45%, #e1e0e1 100%); }
  .edge-band { position: absolute; left: 0; background: var(--blue); }
  .letterhead .edge-band { top: 63px; width: 11px; height: 74px; }
  .contact { position: absolute; font-size: 9px; line-height: 12px; color: var(--ink); }
  .contact p { margin: 0; }
  .contact .gap { height: 5px; }
  .contact .line { display: flex; align-items: center; gap: 5px; }
  .icon { width: 8px; height: 8px; fill: var(--blue); flex: none; }
  .letterhead .contact { left: 59px; top: 61px; }
  .wordmark { position: absolute; font-weight: 600; color: var(--black); white-space: nowrap; }
  .letterhead .wordmark { left: 414px; top: 76px; font-size: 29px; letter-spacing: 5px; }
  .letter { position: absolute; left: 59px; top: 224px; width: 539px; font-family: "Tinos", serif; color: var(--muted); }
  .letter .date { font-size: 12px; margin: 0 0 29px; }
  .letter .recipient { font-size: 12px; line-height: 15.3px; margin: 0 0 25px; }
  .letter .body p { font-size: 10.8px; line-height: 15px; text-align: justify; margin: 0 0 15px; }
  .signature { position: absolute; left: 62px; top: 655px; width: 135px; height: 60px; background: linear-gradient(90deg, #dcdcdc, #e6e6e6); border-radius: 4px; }
  .card-front { left: 822px; top: 326px; width: 345px; height: 197px; background: var(--paper); }
  .card-front .wordmark { left: 25px; top: 22px; font-size: 22px; letter-spacing: 4px; }
  .card-front .edge-band { top: 127px; width: 6px; height: 48px; }
  .holder { position: absolute; left: 26px; top: 127px; }
  .holder .name { margin: 0; font-size: 12px; font-weight: 700; color: var(--blue); line-height: 14px; }
  .holder .role { margin: 0 0 3px; font-size: 8.5px; color: var(--red); line-height: 11px; }
  .holder .addr { margin: 0; font-size: 8.5px; line-height: 11px; color: var(--ink); }
  .card-front .contact { left: 229px; top: 130px; font-size: 8.5px; line-height: 11px; }
  .card-back { left: 822px; top: 555px; width: 345px; height: 196px; background: var(--black); }
  .card-back .wordmark { left: 0; right: 0; top: 76px; text-align: center; font-size: 33px; color: #fff; letter-spacing: 7px; }
</style>
</head>
<body>
<div class="stage">

  <section class="sheet letterhead">
    <div class="edge-band"></div>
    <div class="contact">
      <p>2170 Harlow Crescent</p>
      <p>Brenfield, NY 11920</p>
      <div class="gap"></div>
      <p class="line"><svg class="icon" viewBox="0 0 8 8"><path d="M0 3 Q4 0 8 3 L7 4 L5.5 3 V2 H2.5 V3 L1 4 Z M1.5 5 H6.5 V8 H1.5 Z"/></svg>555 0148 2290</p>
      <p class="line"><svg class="icon" viewBox="0 0 8 8"><path d="M2 0 H6 V8 H2 Z M2.8 1 V6.5 H5.2 V1 Z" fill-rule="evenodd"/></svg>555 0163 7741</p>
      <p class="line"><svg class="icon" viewBox="0 0 8 8"><path d="M0 2 H8 V3 L4 5 L0 3 Z M0 4 L4 6 L8 4 V7 H0 Z"/></svg>hello@pelmora.com</p>
      <p class="line"><svg class="icon" viewBox="0 0 8 8"><circle cx="4" cy="4" r="3.8"/></svg>www.pelmora.com</p>
    </div>
    <div class="wordmark">PELMORA</div>

    <div class="letter">
      <p class="date">Puerto Valmar, Ocober 12,2015</p>
      <p class="recipient">Sr.<br>TOMAS ARRIETA<br>Web Master<br>City</p>
      <div class="body">
        <p>Contrary to popular belief, Lorem Ipsum is not simply random text. It has roots in a piece of classical Latin literature from 45 BC, making it over 2000 years old. Richard Hollowell, a Latin professor at Ashford-Lyle College in Carolina, looked up one of the more obscure Latin words, consectetur, from a Lorem Ipsum passage, and going through the cites of the word in classical literature,</p>
        <p>discovered the undoubtable source. Lorem Ipsum comes from sections 1.10.32 and 1.10.33 of "de Finibus Bonorum et Malorum" (The Extremes of Good and Evil) by Cicero, written in 45 BC. This book is a treatise on the theory of ethics, very popular during the Renaissance. The first line of Lorem Ipsum, "Lorem ipsum dolor sit amet..", comes from a line in section 1.10.32.</p>
        <p>The standard chunk of Lorem Ipsum used since the 1500s is reproduced below for those interested. Sections 1.10.32 and 1.10.33 from "de Finibus Bonorum et Malorum" by Cicero are also reproduced in their exact original form, accompanied by English versions from the 1914 translation by H. Larkwood.</p>
        <p>There are many variations of passages of Lorem Ipsum available, but the majority have suffered alteration in some form, by injected humour, or randomised words which don't look even slightly believable. If you are going to use a passage of Lorem Ipsum, you need to be sure there isn't anything embarrassing hidden in the middle of text.</p>
      </div>
    </div>
    <div class="signature" role="img" aria-label="Handwritten signature of Elan Varga"></div>
  </section>

  <section class="sheet card-front">
    <div class="wordmark">PELMORA</div>
    <div class="edge-band"></div>
    <div class="holder">
      <p class="name">ELAN VARGA</p>
      <p class="role">PRESIDENT</p>
      <p class="addr">2170 Harlow Crescent</p>
      <p class="addr">Brenfield, NY 11920</p>
    </div>
    <div class="contact">
      <p class="line"><svg class="icon" viewBox="0 0 8 8"><path d="M0 3 Q4 0 8 3 L7 4 L5.5 3 V2 H2.5 V3 L1 4 Z M1.5 5 H6.5 V8 H1.5 Z"/></svg>555 0148 2290</p>
      <p class="line"><svg class="icon" viewBox="0 0 8 8"><path d="M2 0 H6 V8 H2 Z M2.8 1 V6.5 H5.2 V1 Z" fill-rule="evenodd"/></svg>555 0163 7741</p>
      <p class="line"><svg class="icon" viewBox="0 0 8 8"><path d="M0 2 H8 V3 L4 5 L0 3 Z M0 4 L4 6 L8 4 V7 H0 Z"/></svg>hello@pelmora.com</p>
      <p class="line"><svg class="icon" viewBox="0 0 8 8"><circle cx="4" cy="4" r="3.8"/></svg>www.pelmora.com</p>
    </div>
  </section>

  <section class="sheet card-back">
    <div class="wordmark">PELMORA</div>
  </section>

</div>
</body>
</html>
```